Local Swedish accounting firm needs a webpage design.

We need a logo design for an accounting firm based in Malmö, Sweden called "Veltrana". We provide a full range of accounting services and have worked closely with startups for many years.
We would like to see an design using the following color scheme.
https://huepiq.io/9b90ba-bfae48-646f58-2541b2-d56501
The design should communicate ease of use and financial safety.

Target Market(s)

We are an accounting firm so are clients are startups and small to medium sized companys

Industry/Entity Type

Accounting

Coding

Coded - Design and coding required

Number of Pages Required

1 page

Font styles to use
Sans Serif

```html
<!DOCTYPE html>
<html lang="en">
<head>
<meta charset="utf-8">
<title>Veltrana – Accounting in Malmö</title>
<link href="https://fonts.googleapis.com/css2?family=Exo+2:wght@600;700;800&family=Open+Sans:wght@400;600&display=swap" rel="stylesheet">
<style>
:root{
  --blue:#2541b2;
  --blue-deep:#1d2a9a;
  --navy:#0f1640;
  --orange:#d56501;
  --lavender:#9b90ba;
  --ink:#222;
  --text:#555;
  --white:#fff;
}
*{box-sizing:border-box;margin:0;padding:0}
html,body{width:1200px;height:4108px;overflow:hidden}
body{position:relative;background:var(--white);font-family:"Open Sans",Arial,sans-serif;color:var(--text)}
.abs{position:absolute}
h1,h2,h3{font-family:"Exo 2",Arial,sans-serif;color:var(--ink)}
.btn{position:absolute;display:inline-block;background:var(--blue-deep);color:var(--white);font:600 13px "Open Sans",Arial,sans-serif;text-transform:uppercase;padding:14px 26px;border-radius:3px}
.btn--orange{background:var(--orange)}

/* hero */
.hero{left:0;top:0;width:1200px;height:560px;overflow:hidden}
.hero__image{position:absolute;inset:0;background:linear-gradient(115deg,#2a0c22 0%,#5a0f1e 35%,#a0162a 60%,#23104a 85%,#0e1a55 100%)}
.hero__cut{position:absolute;left:0;top:0}
.brand{left:112px;top:56px;color:var(--white);font:700 22px "Exo 2",Arial,sans-serif;display:flex;align-items:center;gap:10px}
.brand__dot{width:14px;height:14px;border-radius:50%;background:var(--white)}
.nav{right:112px;top:66px;display:flex;gap:28px;font:600 13px "Open Sans",Arial,sans-serif;color:var(--white);text-transform:uppercase}
.hero__title{left:112px;top:248px;font:800 80px "Exo 2",Arial,sans-serif;color:var(--white);letter-spacing:3px}
.hero__lead{left:112px;top:348px;width:440px;color:var(--white);font-size:15px;line-height:22px}

/* services */
.section-title{width:1200px;left:0;text-align:center;font-size:46px;font-weight:800}
.service__image{position:absolute;width:300px;height:220px}
.service__title{position:absolute;font-size:24px;font-weight:800;text-transform:uppercase}
.service__text{position:absolute;width:430px;font-size:14px;line-height:24px}

/* about */
.about{left:0;top:2520px;width:1200px;height:820px}
.about__title{top:2730px;color:var(--white)}
.about__text{left:150px;top:2818px;width:900px;text-align:center;color:var(--white);font-size:14px;line-height:26px}

/* quote */
.quote__title{left:122px;top:3360px;font-size:46px;font-weight:800}
.quote__text{font-size:14px;line-height:24px;width:430px}

/* footer */
.footer{left:0;top:3640px;width:1200px;height:468px}
.contact{position:absolute;width:240px;text-align:center;color:var(--white)}
.contact__icon{width:60px;height:60px;border:2px solid var(--white);border-radius:50%;margin:0 auto 18px;display:flex;align-items:center;justify-content:center}
.contact__label{font:600 13px "Open Sans",Arial,sans-serif;text-transform:uppercase;margin-bottom:6px}
.contact__value{font-size:17px;line-height:22px}
.partner{left:990px;top:3760px;font:700 20px "Exo 2",Arial,sans-serif;color:var(--navy);display:flex;align-items:center;gap:8px}
.partner__mark{width:16px;height:16px;background:var(--orange)}
.copyright{left:0;top:4060px;width:1200px;text-align:center;color:var(--white);font-size:13px}
</style>
</head>
<body>

<header class="hero abs">
  <div class="hero__image" role="img" aria-label="Photo of financial charts and red stock figures on a screen"></div>
  <svg class="hero__cut" width="1200" height="560" viewBox="0 0 1200 560">
    <polygon points="0,560 0,500 1200,420 1200,560" fill="#fff"/>
    <polygon points="860,446 1200,350 1200,420" fill="#1d2a9a"/>
  </svg>
  <div class="brand abs"><span class="brand__dot"></span>Veltrana</div>
  <nav class="nav abs"><span>Home</span><span>About</span><span>Services</span><span>For entrepreneurs</span><span>GDPR</span><span>Contact</span><span>Login</span></nav>
  <h1 class="hero__title abs">VELTRANA</h1>
  <p class="hero__lead abs">Successful companies know that financial control is a crucial factor. Structure, clear goals and systematic</p>
  <span class="btn" style="left:112px;top:412px">Contact</span>
</header>

<h2 class="section-title abs" style="top:718px">WHAT WE DO</h2>

<div class="service__image" style="left:122px;top:862px;background:linear-gradient(135deg,#0a1b3a 0%,#1c4a7a 55%,#0d2a4e 100%)" role="img" aria-label="Hand touching a digital finance display"></div>
<h3 class="service__title" style="left:570px;top:862px">Accounting services</h3>
<p class="service__text" style="left:570px;top:910px">If you want to devote yourself wholeheartedly to your business, help with current accounting is good advice. Then you do not need to spend time on either administration, accounting or keeping up to date on rule changes. We do it for you.</p>
<span class="btn" style="left:570px;top:1046px">Read more</span>

<h3 class="service__title" style="left:122px;top:1300px">Efficient financial flows</h3>
<p class="service__text" style="left:122px;top:1348px">A well-thought-out basic structure for routines, accounting and data information frees up a lot of time. Valuable time that can be used in a more profitable way in the company. We can help you improve your company's routines. We create a stable basic structure for an efficient financial flow.</p>
<span class="btn" style="left:122px;top:1500px">Read more</span>
<div class="service__image" style="left:660px;top:1270px;width:405px;background:radial-gradient(circle at 50% 50%,#3a7bd6,#0c1e5a 60%,#050c2a)" role="img" aria-label="Glowing digital network graphic"></div>

<div class="service__image" style="left:122px;top:1692px;background:linear-gradient(135deg,#d9e6ef,#9fc4dc 50%,#3b78b8)" role="img" aria-label="Charts and magnifying glass on a desk"></div>
<h3 class="service__title" style="left:570px;top:1720px">Goal-oriented financial management</h3>
<p class="service__text" style="left:570px;top:1768px">Financial information in black and white is usually the best basis for decision-making. Decisions based on assumptions rarely last long. Safe and clear decision-making materials give you the opportunity to anticipate the effects of various action alternatives and develop the company in the right direction.</p>
<span class="btn" style="left:570px;top:1940px">Read more</span>

<h3 class="service__title" style="left:122px;top:2170px">External finance department</h3>
<p class="service__text" style="left:122px;top:2218px">As your external finance department, we add financial expertise in all areas and take overall responsibility for the finance function. You get someone to help you have control over the operational activities, who reacts and gives good advice along the way.</p>
<span class="btn" style="left:122px;top:2356px">Read more</span>
<div class="service__image" style="left:660px;top:2140px;width:405px;background:linear-gradient(135deg,#2a1b6a,#8a2aa0 45%,#1a3c8a)" role="img" aria-label="Colourful abstract city lights"></div>

<svg class="about abs" viewBox="0 0 1200 820" width="1200" height="820">
  <path d="M0,120 C300,40 600,20 900,80 C1020,105 1120,60 1200,0 L1200,720 C900,800 600,640 300,720 C180,750 80,760 0,740 Z" fill="#1d2a9a"/>
  <path d="M0,690 C250,640 520,760 800,700 C1000,660 1120,680 1200,650 L1200,760 C900,820 500,700 0,790 Z" fill="#2541b2"/>
</svg>
<h2 class="section-title about__title abs">ABOUT US</h2>
<p class="about__text abs">Successful companies know that financial control is a crucial factor. Structure, clear goals and systematic follow-up are the guiding principles on the road to good results. We can provide your company with financial expertise in several areas and create and follow up the routines that keep the course straight towards the goals. You get a partner who with commitment analyses and gives advice from a holistic perspective. We are flexible, which means that you can outsource all or part of the company's finance function to us, or hire us as consultants for individual projects. We follow your company's development and add the skills needed at the right time. No matter what you want the collaboration to look like, we help your company to develop in the right direction.</p>
<span class="btn btn--orange" style="left:530px;top:3034px">Read more</span>

<h2 class="quote__title abs">GET A QUOTE</h2>
<p class="quote__text abs" style="left:122px;top:3418px">Nemo enim ipsam voluptatem quia voluptas sit aspernatur aut odit aut fugit, sed quia consequuntur magni dolores eos qui ratione voluptatem sequi nesciunt.</p>
<span class="btn" style="left:122px;top:3500px">Offer link</span>
<p class="quote__text abs" style="left:600px;top:3350px;width:470px">Nemo enim ipsam voluptatem quia voluptas sit aspernatur aut odit aut fugit, sed quia consequuntur magni dolores eos qui ratione voluptatem sequi nesciunt. Neque porro quisquam est, qui dolorem ipsum quia dolor sit amet, consectetur, adipisci velit, sed quia non numquam eius modi tempora incidunt ut labore et dolore magnam aliquam quaerat voluptatem.</p>

<svg class="footer abs" viewBox="0 0 1200 468" width="1200" height="468">
  <polygon points="0,120 700,0 1200,40 1200,468 0,468" fill="#9b90ba"/>
  <polygon points="0,200 900,60 1200,90 1200,468 0,468" fill="#7f74a8"/>
</svg>
<div class="partner abs"><span class="partner__mark"></span>Norrvik Partners</div>

<div class="contact" style="left:128px;top:3820px">
  <div class="contact__icon"><svg width="26" height="26" viewBox="0 0 24 24"><path d="M6.6 10.8a15 15 0 0 0 6.6 6.6l2.2-2.2a1 1 0 0 1 1-.25 11.4 11.4 0 0 0 3.6.57 1 1 0 0 1 1 1V20a1 1 0 0 1-1 1A17 17 0 0 1 3 4a1 1 0 0 1 1-1h3.5a1 1 0 0 1 1 1c0 1.25.2 2.45.57 3.57a1 1 0 0 1-.25 1z" fill="#fff"/></svg></div>
  <div class="contact__label">Telephone</div>
  <div class="contact__value">040-55 20 71</div>
</div>
<div class="contact" style="left:480px;top:3820px">
  <div class="contact__icon"><svg width="26" height="26" viewBox="0 0 24 24"><path d="M3 5h18v14H3z" fill="none" stroke="#fff" stroke-width="2"/><path d="M3 6l9 7 9-7" fill="none" stroke="#fff" stroke-width="2"/></svg></div>
  <div class="contact__label">Email</div>
  <div class="contact__value">info@veltrana.se</div>
</div>
<div class="contact" style="left:832px;top:3820px">
  <div class="contact__icon"><svg width="26" height="26" viewBox="0 0 24 24"><path d="M12 2a7 7 0 0 0-7 7c0 5 7 13 7 13s7-8 7-13a7 7 0 0 0-7-7zm0 9.5A2.5 2.5 0 1 1 12 6.5a2.5 2.5 0 0 1 0 5z" fill="#fff"/></svg></div>
  <div class="contact__label">Address</div>
  <div class="contact__value">Lindblomsgatan 7<br>211 40 Malmö</div>
</div>

<p class="copyright abs">© 2020 All Rights Reserved</p>

</body>
</html>
```